Website for SaaS CRM software

We require a cool website for a new SaaS CRM software. The design needs to be slick and modern. I quite like the look of sites like PostOtter.

The character 'Marla' in the video is the main character which we would like to incorporate on each page if possible. Like the chimp on Postotter website.

'Sign Up Free' button or form to feature throughout the site so we have a strong call to action.

Here is a short video which will give you an idea of the software:
https://clipvault.example/83920417
Password: trelbq

You can login to the user software (backend) for screen grabs and to see what the software is all about:
www.taskloomhq.example
Username: tenant7
Password: tenant7

Please note: The website is for the front end which is where we sell the software and NOT once the user has logged in.

Target Market(s)

Small businesses, freelancers, designers, 1-man businesses

Industry/Entity Type

Software

Requirements
Must have
• 1. Opt-in box for getting started for free:

'Sign up for your Free account'

2. Logos for social media : Fb/Chirper/YouTube/LinkedIn / G+
3. Chatterbook 'LIKE' button
4.The Navigation Bar should always be on display at the top when scrolling
5. Login button near the Navigation Bar
6. Login page or pop-up should also have 'Forgot Password' link which prompts them to enter their email so a password can be emailed to them.

5 pages & a blog in total. The pages we require are:

HOME
- Heading 'Easy to use small business software'
- Should have a video placeholder and some bullet points or tick marks for key features. The video (from YouTube) should open up on a bigger lightbox and the background greyed out.
- Sign up box to have the fields for First Name, Company Name, Email & Password with a check box for 'I agree with Terms & Conditions'

TOUR
Sub-Navigation bar at the top or side bar with the headings for each module i.e CONTACTS, QUOTES, JOBS, DIARY, SALES, PURCHASES, PRODUCTS, REPORTS
Each module with need to have a placeholder for an image or video and 1 paragraph of text explaining key features. Please see http://postotter.example/features/

See how the Navigation buttons stay visible at all times and changes to the next button when scrolling: http://postotter.example/features/

No side bar on this page.

PRICING
Pricing table of 3 to 4 columns with a button at the bottom. This software is a monthly subscription, so we need to show the $/month for each Plan at the top with the name of the Plan
The plans are:
Bronze: Free
Silver: $20/month
Gold: $40 / month
Platinum: $75 / month

No side bar on this page.

Heading at the bottom: 'No minimum contract. Cancel anytime.'

SUPPORT PAGE
This to a contact form to submit a ticket for tech support. We also need a 2-column list for videos which we will put up. The video open up on a lightbox in bigger size.

No side bar on this page.

CONTACT
Contact details i.e name, address, telephone, email & a contact form
No side bar on this page.

BLOG
Pagecraft blog. I love the way the headings, paragraph, font, line spacing, colours are on the PostOtter blog.

Need a side bar.

```html
<!DOCTYPE html>
<html lang="en">
<head>
<meta charset="utf-8">
<title>Blog – Taskloom</title>
<link href="https://fonts.googleapis.com/css2?family=Montserrat:wght@400;500;600;700;800&family=Open+Sans:wght@400;600;700&display=swap" rel="stylesheet">
<style>
:root{
  --sky:#62c4df;
  --page:#ebebeb;
  --card:#ffffff;
  --ink:#222222;
  --muted:#6b6b6b;
  --text:#555555;
  --accent:#1ba8d4;
  --rule:#dcdcdc;
  --panel:#f7f7f7;
  --footer:#1b2226;
  --button:#4fb3d6;
}
*{box-sizing:border-box;margin:0;padding:0}
html,body{width:805px;height:1200px;overflow:hidden}
body{position:relative;background:var(--page);font-family:"Open Sans",Arial,sans-serif;color:var(--ink)}
a{color:inherit;text-decoration:none}

.top-band{position:absolute;left:0;top:0;width:805px;height:105px;background:var(--sky)}
.brand{position:absolute;left:100px;top:14px;font-family:"Montserrat",sans-serif;font-weight:800;font-size:33px;letter-spacing:-1px;color:#111;display:flex;align-items:center;gap:8px}
.brand-dot{width:16px;height:16px;border-radius:50%;background:#fff}

.sheet{position:absolute;left:100px;top:68px;width:602px;height:1082px;background:var(--card);border-radius:4px 4px 0 0;box-shadow:0 1px 3px rgba(0,0,0,.12)}

.main-nav{position:absolute;left:100px;top:68px;width:602px;height:38px;border-bottom:1px solid var(--rule);border-radius:4px 4px 0 0;background:linear-gradient(#fff,#f4f4f4)}
.main-nav ul{list-style:none;display:flex;height:100%;padding-left:6px}
.main-nav li{font-family:"Montserrat",sans-serif;font-size:13.5px;color:#444;padding:0 10px;line-height:38px;border-right:1px solid #e6e6e6}
.main-nav li.is-current{color:var(--accent)}
.like-chip{position:absolute;left:466px;top:12px;display:flex;gap:2px;font-size:7px;font-family:Arial,sans-serif}
.like-chip span{border:1px solid #c9cfdc;background:#eef1f7;padding:1px 3px;color:#3b5998}
.like-chip span+span{background:#fff;color:#333;border-color:#ccc}
.login-btn{position:absolute;left:525px;top:6px;width:70px;height:26px;border-radius:13px;border:2px solid #d6d6d6;background:linear-gradient(#fff,#ececec);font-family:"Montserrat",sans-serif;font-weight:700;font-size:11px;color:#555;text-align:center;line-height:22px;letter-spacing:.5px}

.page-title{position:absolute;left:113px;top:117px;font-family:"Montserrat",sans-serif;font-weight:700;font-size:19px;color:var(--accent)}

.post{position:absolute;left:113px;width:426px;height:477px}
.post-avatar{position:absolute;left:0;top:4px;width:33px;height:33px;background:linear-gradient(#9b9b9b,#5a5048)}
.post-title{position:absolute;left:43px;top:0;width:340px;font-family:"Montserrat",sans-serif;font-weight:700;font-size:13.5px;line-height:15px;color:var(--accent)}
.post-meta{position:absolute;left:43px;top:35px;font-size:9px;color:var(--muted)}
.post-body{position:absolute;left:0;top:56px;width:426px;height:421px;background:var(--panel);border:1px solid #e4e4e4;border-radius:3px}
.post-figure{position:absolute;left:12px;top:12px;width:290px;height:180px;background:linear-gradient(135deg,#fbf8c8,#f6f0a8 60%,#cfd8e8)}
.post-text{position:absolute;left:11px;top:202px;width:294px;font-size:8.4px;line-height:14.2px;color:var(--text)}
.read-more{position:absolute;left:11px;top:396px;font-size:8.5px;color:var(--accent)}
.post-aside{position:absolute;left:317px;top:10px;width:92px}
.comments{font-family:"Montserrat",sans-serif;font-size:10.5px;color:#444;border-bottom:1px dotted #999;display:inline-block;width:70px;padding-bottom:1px}
.share-row{display:flex;gap:3px;margin-top:3px;font-size:6.5px;font-family:Arial,sans-serif}
.share-row:first-of-type{margin-top:20px}
.share-btn{border:1px solid #c7c7c7;background:#f0f0f0;padding:1px 3px;border-radius:2px;color:#333}
.share-count{border:1px solid #ccc;background:#fff;padding:1px 3px;color:#555}
.tags-label{margin-top:13px;font-family:"Montserrat",sans-serif;font-size:10.5px;color:#444}
.tag-list{list-style:none;margin-top:6px}
.tag-list li{width:89px;height:17px;margin-bottom:4px;background:#fff;border:1px solid #e1e1e1;border-radius:2px;font-size:8px;font-weight:700;color:#555;padding-left:6px;line-height:15px}

.sidebar{position:absolute;left:549px;top:154px;width:150px;height:468px;border-left:1px solid var(--rule);padding-left:9px}
.subscribe-btn{display:block;width:131px;height:22px;border-radius:3px;background:linear-gradient(#6cc5e4,var(--button));color:#fff;font-size:8.5px;font-weight:700;text-align:center;line-height:22px;border:1px solid #3f9fc2}
.side-heading{font-family:"Montserrat",sans-serif;font-size:11.5px;font-weight:600;color:#444}
.authors-heading{margin-top:10px}
.author-grid{display:grid;grid-template-columns:repeat(3,33px);column-gap:11px;row-gap:9px;margin-top:10px}
.author-grid span{width:33px;height:33px;background:linear-gradient(#d8d4cf,#8a7a6c)}
.web-heading{margin-top:26px}
.link-list{list-style:none;margin-top:6px}
.link-list li{font-size:8px;font-weight:700;color:#333;line-height:14.5px}
.rss-heading{margin-top:15px}

.site-footer{position:absolute;left:0;top:1143px;width:805px;height:57px;background:var(--footer)}
.copyright{position:absolute;left:100px;top:24px;font-size:8.5px;color:#e8e8e8}
.social-links{position:absolute;left:578px;top:19px;display:flex;gap:3px}
.social-links span{width:22px;height:22px;border-radius:4px}
</style>
</head>
<body>
<div class="top-band"></div>
<a class="brand" href="#">taskloom<span class="brand-dot"></span></a>

<div class="sheet"></div>
<nav class="main-nav">
  <ul>
    <li>Home</li><li>Tour</li><li>Pricing</li><li>Support</li><li>Contact</li><li class="is-current">Blog</li>
  </ul>
  <div class="like-chip"><span>Like</span><span>3.6k</span></div>
  <a class="login-btn" href="#">LOGIN</a>
</nav>

<h1 class="page-title">Blog</h1>

<article class="post" style="top:148px">
  <div class="post-avatar" role="img" aria-label="Author portrait"></div>
  <h2 class="post-title">Nunc consequat dolor eget nunc rutrum eu posuere arcu aliquet.</h2>
  <p class="post-meta">Posted by Theo on Dec 18, 2012</p>
  <div class="post-body">
    <div class="post-figure" role="img" aria-label="Illustration of the mascot working at a laptop in an office"></div>
    <p class="post-text">Sed ut perspiciatis unde omnis iste natus error sit voluptatem accusantium doloremque laudantium, totam rem aperiam, eaque ipsa quae ab illo inventore veritatis et quasi architecto beatae vitae dicta sunt explicabo. Nemo enim ipsam voluptatem quia voluptas sit aspernatur aut odit aut fugit, sed quia consequuntur magni dolores eos qui ratione voluptatem sequi nesciunt. Neque porro quisquam est, qui dolorem ipsum quia dolor sit amet, consectetur, adipisci velit, sed quia non numquam eius modi tempora incidunt ut labore et dolore magnam aliquam quaerat voluptatem. Ut enim ad minima veniam, quis nostrum exercitationem ullam corporis suscipit laboriosam, nisi ut aliquid ex ea commodi consequatur? Quis autem vel eum iure reprehenderit qui in ea voluptate velit esse quam nihil molestiae consequatur, vel illum qui dolorem eum fugiat quo voluptas nulla pariatur?</p>
    <a class="read-more" href="#">Read more...</a>
    <aside class="post-aside">
      <span class="comments">13 Comments</span>
      <div class="share-row"><span class="share-btn">+1</span><span class="share-count">7</span></div>
      <div class="share-row"><span class="share-btn">Share</span><span class="share-count">99</span></div>
      <div class="share-row"><span class="share-btn">Like</span><span class="share-count">59</span><span class="share-btn">Send</span></div>
      <p class="tags-label">Tags</p>
      <ul class="tag-list"><li>Duis</li><li>consequat</li><li>hendrerit</li><li>mauris</li><li>viverra</li><li>congue</li></ul>
    </aside>
  </div>
</article>

<article class="post" style="top:653px">
  <div class="post-avatar" role="img" aria-label="Author portrait"></div>
  <h2 class="post-title">Nunc consequat dolor eget nunc rutrum eu posuere arcu aliquet.</h2>
  <p class="post-meta">Posted by Theo on Dec 18, 2012</p>
  <div class="post-body">
    <div class="post-figure" role="img" aria-label="Illustration of the mascot working at a laptop in an office"></div>
    <p class="post-text">Sed ut perspiciatis unde omnis iste natus error sit voluptatem accusantium doloremque laudantium, totam rem aperiam, eaque ipsa quae ab illo inventore veritatis et quasi architecto beatae vitae dicta sunt explicabo. Nemo enim ipsam voluptatem quia voluptas sit aspernatur aut odit aut fugit, sed quia consequuntur magni dolores eos qui ratione voluptatem sequi nesciunt. Neque porro quisquam est, qui dolorem ipsum quia dolor sit amet, consectetur, adipisci velit, sed quia non numquam eius modi tempora incidunt ut labore et dolore magnam aliquam quaerat voluptatem. Ut enim ad minima veniam, quis nostrum exercitationem ullam corporis suscipit laboriosam, nisi ut aliquid ex ea commodi consequatur? Quis autem vel eum iure reprehenderit qui in ea voluptate velit esse quam nihil molestiae consequatur, vel illum qui dolorem eum fugiat quo voluptas nulla pariatur?</p>
    <a class="read-more" href="#">Read more...</a>
    <aside class="post-aside">
      <span class="comments">13 Comments</span>
      <div class="share-row"><span class="share-btn">+1</span><span class="share-count">7</span></div>
      <div class="share-row"><span class="share-btn">Share</span><span class="share-count">99</span></div>
      <div class="share-row"><span class="share-btn">Like</span><span class="share-count">59</span><span class="share-btn">Send</span></div>
      <p class="tags-label">Tags</p>
      <ul class="tag-list"><li>Duis</li><li>consequat</li><li>hendrerit</li><li>mauris</li><li>viverra</li><li>congue</li></ul>
    </aside>
  </div>
</article>

<aside class="sidebar">
  <a class="subscribe-btn" href="#">Subscribe to Email Updtes</a>
  <h3 class="side-heading authors-heading">Authors</h3>
  <div class="author-grid">
    <span role="img" aria-label="Author portrait"></span><span role="img" aria-label="Author portrait"></span><span role="img" aria-label="Author portrait"></span>
    <span role="img" aria-label="Author portrait"></span><span role="img" aria-label="Author portrait"></span><span role="img" aria-label="Author portrait"></span>
    <span role="img" aria-label="Author portrait"></span><span role="img" aria-label="Author portrait"></span><span role="img" aria-label="Author portrait"></span>
    <span role="img" aria-label="Author portrait"></span><span role="img" aria-label="Author portrait"></span><span role="img" aria-label="Author portrait"></span>
    <span role="img" aria-label="Author portrait"></span><span role="img" aria-label="Author portrait"></span><span role="img" aria-label="Author portrait"></span>
    <span role="img" aria-label="Author portrait"></span><span role="img" aria-label="Author portrait"></span><span role="img" aria-label="Author portrait"></span>
  </div>
  <h3 class="side-heading web-heading">Around the Web</h3>
  <ul class="link-list">
    <li>Taskloom Creative</li>
    <li>Taskloom on Chatterbook</li>
    <li>Taskloom on Snapstream</li>
    <li>Taskloom on Postwell</li>
    <li>Taskloom on Chirper</li>
  </ul>
  <h3 class="side-heading rss-heading">RSS</h3>
  <ul class="link-list"><li>Subscribe to PostOtter Blog</li></ul>
</aside>

<footer class="site-footer">
  <p class="copyright">© 2012 Taskloom, All rights reserved.</p>
  <div class="social-links">
    <span style="background:#3b6aa8"></span>
    <span style="background:#4fb3d6"></span>
    <span style="background:#2a7fb3"></span>
    <span style="background:#d23a2e"></span>
    <span style="background:#3c7fd0"></span>
  </div>
</footer>
</body>
</html>
```